BRIGHT SEAL INSULATION

WE NEED A TRUCK WRAP DESIGN.
WE ARE A SPRAY FOAM COMPANY.
Phone: (555)318-2096
email: info@brightsealinsulation.example
www.brightsealinsulation.example
Instagram: brightsealinsulation

```html
<!DOCTYPE html>
<html lang="en">
<head>
<meta charset="utf-8">
<title>Bright Seal Insulation – Truck Wrap</title>
<link href="https://fonts.googleapis.com/css2?family=Montserrat:wght@300;500;700&display=swap" rel="stylesheet">
<style>
  :root{
    --brand-green:#0a7a0a;
    --ink:#0d0d0d;
    --paper:#f4f4f4;
    --white:#ffffff;
    --photo-light:#d9d4c8;
    --photo-dark:#a89c86;
  }
  *{margin:0;padding:0;box-sizing:border-box}
  html,body{width:1200px;height:1200px;overflow:hidden;background:var(--paper);font-family:"Montserrat",sans-serif}
  .canvas{position:relative;width:1200px;height:1200px}
  .panel{position:absolute;overflow:hidden;background:var(--white)}
  .panel svg.art{position:absolute;inset:0;width:100%;height:100%}
  .side-panel{left:50px;top:40px;width:1100px;height:460px}
  .rear-panel{left:378px;top:560px;width:443px;height:513px}
  .wordmark{position:absolute;color:var(--ink);font-weight:700;line-height:1;white-space:nowrap}
  .tagline{position:absolute;color:var(--brand-green);font-weight:300;line-height:1;white-space:nowrap}
  .phone{position:absolute;font-weight:700;line-height:1;color:var(--ink);white-space:nowrap}
  .phone .local{color:var(--brand-green)}
  .contact-list{position:absolute;list-style:none;font-weight:500;color:var(--ink)}
  .contact-list li{display:flex;align-items:center;gap:7px;margin-bottom:12px;font-size:19px}
  .contact-list svg{width:20px;height:20px;flex:none}
  .cloud-name{position:absolute;color:var(--white);font-weight:700;line-height:1.05;text-align:center;white-space:nowrap}

  .side-panel .wordmark{left:34px;top:86px;font-size:90px}
  .side-panel .tagline{left:178px;top:184px;font-size:42px;letter-spacing:17px}
  .side-panel .contact-list{left:40px;top:268px}
  .side-panel .phone{left:34px;top:360px;font-size:56px}
  .side-panel .cloud-name{left:740px;top:150px;width:340px;font-size:40px}

  .rear-panel .cloud-name{left:0;top:150px;width:443px;font-size:38px}
  .rear-panel .wordmark{left:0;width:443px;text-align:center;top:345px;font-size:47px}
  .rear-panel .tagline{left:0;width:443px;text-align:center;top:396px;font-size:24px;letter-spacing:11px}
  .rear-panel .phone{left:0;width:443px;text-align:center;top:438px;font-size:44px}
</style>
</head>
<body>
<main class="canvas">

  <section class="panel side-panel" aria-label="Truck side panel">
    <svg class="art" viewBox="0 0 1100 460" preserveAspectRatio="none">
      <defs>
        <linearGradient id="sidePhoto" x1="0" y1="0" x2="1" y2="1">
          <stop offset="0" stop-color="var(--photo-light)"/>
          <stop offset="1" stop-color="var(--photo-dark)"/>
        </linearGradient>
        <linearGradient id="gunTone" x1="0" y1="0" x2="0" y2="1">
          <stop offset="0" stop-color="#2a2a2a" stop-opacity=".55"/>
          <stop offset="1" stop-color="#2a2a2a" stop-opacity=".35"/>
        </linearGradient>
      </defs>
      <rect class="photo-backdrop" width="1100" height="460" fill="url(#sidePhoto)" role="img" aria-label="Photo of an installer in a white protective suit spraying foam insulation between attic rafters"/>
      <rect width="1100" height="460" fill="#ffffff" opacity=".35"/>
      <rect class="spray-gun" x="440" y="235" width="150" height="205" rx="20" fill="url(#gunTone)" role="img" aria-label="Illustration of a spray foam gun"/>
      <g class="spray-lines" stroke="var(--brand-green)" stroke-width="5" stroke-linecap="round">
        <line x1="605" y1="250" x2="705" y2="208"/>
        <line x1="605" y1="255" x2="705" y2="238"/>
        <line x1="605" y1="260" x2="705" y2="268"/>
        <line x1="605" y1="265" x2="705" y2="298"/>
      </g>
      <path class="foam-cloud" fill="var(--brand-green)"
        d="M712 0 H1100 V460 H1030
           C1020 425 990 405 955 405
           C940 435 905 450 875 425
           C850 445 810 440 795 405
           C760 410 720 385 725 345
           C690 335 680 285 705 262
           C680 240 685 190 720 175
           C695 150 705 100 730 90
           C700 70 705 25 712 0 Z"/>
    </svg>
    <p class="cloud-name">BRIGHT SEAL<br>INSULATION</p>
    <h1 class="wordmark">BRIGHT SEAL</h1>
    <p class="tagline">INSULATION</p>
    <ul class="contact-list">
      <li>
        <svg viewBox="0 0 20 20" aria-hidden="true"><circle cx="10" cy="10" r="10" fill="var(--brand-green)"/><rect x="4.5" y="6.5" width="11" height="7.5" rx="1" fill="none" stroke="#fff" stroke-width="1.4"/><path d="M4.8 7 10 11l5.2-4" fill="none" stroke="#fff" stroke-width="1.4"/></svg>
        info@brightsealinsulation.example
      </li>
      <li>
        <svg viewBox="0 0 20 20" aria-hidden="true"><circle cx="10" cy="10" r="10" fill="var(--brand-green)"/></svg>
        brightsealinsulation
      </li>
    </ul>
    <p class="phone">(555)<span class="local">318-2096</span></p>
  </section>

  <section class="panel rear-panel" aria-label="Truck rear panel">
    <svg class="art" viewBox="0 0 443 513" preserveAspectRatio="none">
      <defs>
        <linearGradient id="rearPhoto" x1="0" y1="0" x2="1" y2="1">
          <stop offset="0" stop-color="var(--photo-light)"/>
          <stop offset="1" stop-color="var(--photo-dark)"/>
        </linearGradient>
      </defs>
      <rect class="photo-backdrop" width="443" height="513" fill="url(#rearPhoto)" role="img" aria-label="Photo of an installer spraying foam insulation in a framed attic"/>
      <rect width="443" height="513" fill="#ffffff" opacity=".35"/>
      <path class="foam-cloud" fill="var(--brand-green)"
        d="M0 0 H443 V283
           C420 300 390 300 372 285
           C360 320 320 335 295 315
           C275 345 230 350 210 325
           C185 345 140 340 130 310
           C95 330 55 315 55 280
           C25 285 5 270 0 255 Z"/>
    </svg>
    <p class="cloud-name">BRIGHT SEAL<br>INSULATION</p>
    <h2 class="wordmark">BRIGHT SEAL</h2>
    <p class="tagline">INSULATION</p>
    <p class="phone">(555)<span class="local">318-2096</span></p>
  </section>

</main>
</body>
</html>
```